Bref créative
Law firm stationary package
Letterhead, business card, envelope
Professional
Theodore R. Wexley
Attorney at Law
5183 Poldin Lane, Suite A
P.O. Box 81947
Cincinnati, OH 45867
Ted@WexleyCounsel.example
www.WexleyCounsel.example
Please create business card, letterhead, and envelope designs.
Focus on clean, professional design for this corporate law firm. Stay away from watermarks, waves, or anything that is too ink-intensive. You may use either or both of the attached logos.
Main logo
Inverse of logo, use is optional

```html
<!DOCTYPE html>
<html lang="en">
<head>
<meta charset="utf-8">
<title>Wexley Stationery Package</title>
<link href="https://fonts.googleapis.com/css2?family=Cinzel:wght@400;600&family=Open+Sans:wght@400;600&display=swap" rel="stylesheet">
<style>
  :root{
    --navy:#3d3a80;
    --navy-dark:#2f2c6a;
    --grey:#8d8d92;
    --paper:#ffffff;
    --ink:#3a3a48;
    --stage-a:#2a3140;
    --stage-b:#10141c;
  }
  *{margin:0;padding:0;box-sizing:border-box}
  html,body{width:1200px;height:631px;overflow:hidden}
  body{
    position:relative;
    background:radial-gradient(ellipse at 50% 45%,var(--stage-a),var(--stage-b));
    font-family:"Open Sans",sans-serif;color:var(--ink);
  }
  .sheet{position:absolute;background:var(--paper);box-shadow:0 3px 10px rgba(0,0,0,.45);overflow:hidden}
  .brand{display:flex;align-items:center;gap:6px}
  .brand-mark{background:var(--navy);flex:none}
  .brand-name{font-family:"Cinzel",serif;font-weight:400;color:var(--navy);letter-spacing:.04em;line-height:1}
  .brand-tag{font-size:4px;color:var(--grey);letter-spacing:.1em;text-transform:uppercase;margin-top:2px}
  .small{font-size:4.2px;line-height:6.4px;color:var(--ink)}
  .band{position:absolute;left:0;right:0;background:var(--navy);display:flex;align-items:center}
  .band-url{color:#fff;font-size:4.6px;letter-spacing:.35em;flex:1;text-align:center}
  .band-end{background:var(--grey);height:100%;width:18%}

  /* business cards */
  .card{left:38px;width:166px;height:96px}
  .card-front{top:233px}
  .card-front .person{position:absolute;left:10px;top:10px}
  .card-front .person b{display:block;font-size:6px;color:var(--ink);font-weight:600}
  .card-front .person span{font-size:4px;color:var(--grey)}
  .card-front .contact{position:absolute;left:62px;top:36px}
  .card-front .band{bottom:10px;height:14px;padding-left:10px}
  .card-front .band .brand-name{color:#fff;font-size:8px}
  .card-front .band .brand-mark{background:#fff;width:7px;height:7px}
  .card-back-blue{top:341px;background:var(--navy)}
  .card-back-blue .center,.card-back-white .center{position:absolute;inset:0;display:flex;align-items:center;justify-content:center}
  .card-back-blue .brand-name{color:#fff;font-size:13px}
  .card-back-blue .brand-mark{background:#fff;width:10px;height:10px}
  .card-back-blue .stripe{position:absolute;left:0;right:0;bottom:12px;height:8px;background:var(--navy-dark)}
  .card-back-white{top:446px;height:92px}
  .card-back-white .brand-name{font-size:13px}
  .card-back-white .brand-mark{width:10px;height:10px}

  /* letterhead */
  .letterhead{left:247px;top:48px;width:396px;height:526px}
  .letterhead .head-brand{position:absolute;left:22px;top:22px}
  .letterhead .head-brand .brand-mark{width:16px;height:16px}
  .letterhead .head-brand .brand-name{font-size:14px}
  .letterhead .rule{position:absolute;left:43px;top:22px;width:1px;height:22px;background:var(--grey);opacity:.5}
  .letterhead .address{position:absolute;left:270px;top:22px}
  .letterhead .band{bottom:18px;height:16px}
  .letterhead .band-end{display:flex;align-items:center;justify-content:center}
  .letterhead .band-end i{width:7px;height:7px;background:#fff;display:block}

  /* envelopes */
  .env{left:703px;width:468px}
  .env-back{top:103px;height:216px}
  .env-back svg{position:absolute;inset:0}
  .env-back .flap-brand{position:absolute;left:0;right:0;top:44px;display:flex;justify-content:center}
  .env-back .flap-brand .brand-name{color:#fff;font-size:11px}
  .env-back .flap-brand .brand-mark{background:#fff;width:9px;height:9px}
  .env-back .seal-brand{position:absolute;left:0;right:0;top:146px;display:flex;justify-content:center}
  .env-back .seal-brand .brand-name{font-size:11px}
  .env-back .seal-brand .brand-mark{width:9px;height:9px}
  .env-front{top:425px;height:168px}
  .env-front .head-brand{position:absolute;left:16px;top:16px}
  .env-front .head-brand .brand-mark{width:14px;height:14px}
  .env-front .head-brand .brand-name{font-size:13px}
  .env-front .address{position:absolute;left:38px;top:48px}
  .env-front .band{bottom:14px;height:14px}
</style>
</head>
<body>

  <!-- business card: front -->
  <section class="sheet card card-front">
    <div class="person"><b>Theodore R. Wexley</b><span>Attorney at Law</span></div>
    <div class="contact small">
      5183 Poldin Lane, Suite A<br>P.O. Box 81947<br>Cincinnati, OH 45867<br>
      Tel (555) 014-2290<br>Ted@WexleyCounsel.example
    </div>
    <div class="band">
      <div class="brand"><span class="brand-mark"></span><span class="brand-name">Wexley</span></div>
    </div>
  </section>

  <!-- business card: back, blue -->
  <section class="sheet card card-back-blue">
    <div class="center"><div class="brand"><span class="brand-mark"></span><span class="brand-name">Wexley</span></div></div>
    <div class="stripe"></div>
  </section>

  <!-- business card: back, white -->
  <section class="sheet card card-back-white">
    <div class="center"><div class="brand"><span class="brand-mark"></span><span class="brand-name">Wexley</span></div></div>
  </section>

  <!-- letterhead -->
  <section class="sheet letterhead">
    <div class="head-brand brand">
      <span class="brand-mark"></span>
      <div><div class="brand-name">Wexley</div><div class="brand-tag">Attorney at Law</div></div>
    </div>
    <div class="address small">
      5183 Poldin Lane, Suite A<br>P.O. Box 81947<br>Cincinnati, OH 45867<br>
      Tel (555) 014-2290<br>Fax (555) 014-2291<br>Ted@WexleyCounsel.example
    </div>
    <div class="band">
      <span class="band-url">www.WexleyCounsel.example</span>
      <span class="band-end"><i></i></span>
    </div>
  </section>

  <!-- envelope: back with flap -->
  <section class="sheet env env-back">
    <svg width="468" height="216" viewBox="0 0 468 216" aria-hidden="true">
      <polygon points="0,0 468,0 468,22 234,110 0,22" fill="var(--navy)"/>
      <polyline points="0,62 234,150 468,62" fill="none" stroke="#d4d4da" stroke-width="1"/>
      <polyline points="0,216 160,120" fill="none" stroke="#e2e2e6" stroke-width="1"/>
      <polyline points="468,216 308,120" fill="none" stroke="#e2e2e6" stroke-width="1"/>
    </svg>
    <div class="flap-brand brand"><span class="brand-mark"></span><span class="brand-name">Wexley</span></div>
    <div class="seal-brand brand"><span class="brand-mark"></span><span class="brand-name">Wexley</span></div>
  </section>

  <!-- envelope: front -->
  <section class="sheet env env-front">
    <div class="head-brand brand">
      <span class="brand-mark"></span>
      <div><div class="brand-name">Wexley</div><div class="brand-tag">Attorney at Law</div></div>
    </div>
    <div class="address small">5183 Poldin Lane, Suite A<br>P.O. Box 81947<br>Cincinnati, OH 45867</div>
    <div class="band">
      <span class="band-url">www.WexleyCounsel.example</span>
      <span class="band-end"></span>
    </div>
  </section>

</body>
</html>
```